Professional Label needed for Meadowpaw Snack Co

I make 100% organic dog treats. Wheat and gluten free.

I will be packaging them in a window kraft bag. I need a nicely designed label to place on each bag. The name of my company is The Meadowpaw Snack Company. All ingredients are organic and no preservatives are used. They are a healthy alternative to "assembly line" treats made by large companies.

Target Market(s)

Dog Owners

Industry/Entity Type

Pet

Font styles to use
Serif

Colors
00a990

Requirements
Must have
• can use a dog paw - see attached files. Dog themed, 100%
• Organic Dog Treats.
• No preservatives, nothing artificial, no corn, wheat or soy, made in Texas, USA with 100% organic ingredients. Non GMO
• Must have "dog treat" somewhere.
• "The Meadowpaw Snack Co." font size needs to be bigger than anything else.
Nice to have
• I like teal and brown
• I'm open to anything really as long as its dog themed

```html
<!DOCTYPE html>
<html lang="en">
<head>
<meta charset="utf-8">
<title>Meadowpaw Snack Co. – Treat Bag Label</title>
<link href="https://fonts.googleapis.com/css2?family=Carlito:wght@400;700&family=Arvo&display=swap" rel="stylesheet">
<style>
  :root {
    --page: #ffffff;
    --ink: #111111;
    --frame-line: #555555;
    --kraft: #8b5e3c;
    --header-brown: #6e4d35;
    --header-brown-dark: #5a3d29;
    --mint: #80c99f;
    --copy-brown: #8a5a35;
    --paw-brown: #653a17;
    --teal: #10a48c;
    --badge-green: #22b35e;
    --badge-ribbon: #1e8f4a;
  }
  html, body {
    margin: 0;
    padding: 0;
    width: 1200px;
    height: 848px;
    overflow: hidden;
    background: var(--page);
  }
  .sheet {
    position: relative;
    width: 1200px;
    height: 848px;
    font-family: "Carlito", "Calibri", sans-serif;
  }
  .label {
    position: absolute;
    width: 720px;
    height: 431px;
    box-sizing: border-box;
    border: 1px solid var(--frame-line);
    background: var(--page);
    transform-origin: 0 0;
  }
  .label--preview { left: 43px; top: 38px; transform: scale(0.5); border-width: 2px; }
  .label--full { left: 397px; top: 327px; }
  .label__border {
    position: absolute;
    left: 9px; top: 9px;
    width: 700px; height: 414px;
    box-sizing: border-box;
    border: 6px solid var(--kraft);
  }
  .label__header {
    position: absolute;
    left: 20px; top: 14px;
    width: 679px; height: 222px;
    background: linear-gradient(180deg, var(--header-brown) 0%, var(--header-brown-dark) 100%);
    display: flex;
    align-items: center;
    justify-content: center;
  }
  .brand-name {
    font-family: "Carlito", "Calibri", sans-serif;
    font-weight: 700;
    font-size: 44px;
    color: var(--mint);
    margin: 0;
    letter-spacing: 0.2px;
  }
  .claims {
    position: absolute;
    left: 31px; top: 245px;
    margin: 0;
    font-weight: 700;
    font-size: 27px;
    line-height: 31px;
    color: var(--copy-brown);
  }
  .origin-pill {
    position: absolute;
    left: 27px; top: 350px;
    width: 188px; height: 56px;
    border-radius: 28px;
    background: var(--teal);
    color: #ffffff;
    font-family: "Arvo", serif;
    text-align: center;
    line-height: 1;
  }
  .origin-pill__small { display: block; font-size: 20px; padding-top: 5px; }
  .origin-pill__large { display: block; font-size: 29px; margin-top: 1px; }
  .organic-badge {
    position: absolute;
    left: 276px; top: 292px;
    width: 150px; height: 118px;
  }
  .paw-icon {
    position: absolute;
    left: 512px; top: 272px;
    width: 120px; height: 108px;
  }
  .product-line {
    position: absolute;
    left: 481px; top: 380px;
    margin: 0;
    font-weight: 700;
    font-size: 29px;
    color: var(--copy-brown);
  }
  .size-caption {
    position: absolute;
    left: 96px; top: 276px;
    margin: 0;
    font-size: 32px;
    color: var(--ink);
  }
</style>
</head>
<body>
<main class="sheet">

  <section class="label label--preview" aria-label="Label preview, small scale">
    <div class="label__border"></div>
    <div class="label__header" role="img" aria-label="Brown header with swirl and paw-print pattern and a mint dog bone holding the company name">
      <p class="brand-name">The Meadowpaw Snack Co.</p>
    </div>
    <p class="claims">No preservatives- nothing artificial<br>No corn, wheat or soy</p>
    <div class="origin-pill"><span class="origin-pill__small">Made in</span><span class="origin-pill__large">Texas, USA</span></div>
    <svg class="organic-badge" viewBox="0 0 150 118" aria-hidden="true">
      <path d="M5 82 L40 70 L40 98 Z M145 82 L110 70 L110 98 Z" fill="var(--badge-ribbon)"/>
      <circle cx="75" cy="58" r="55" fill="var(--badge-green)"/>
    </svg>
    <svg class="paw-icon" viewBox="0 0 120 108" aria-hidden="true">
      <ellipse cx="15" cy="42" rx="13" ry="19" fill="var(--paw-brown)"/>
      <ellipse cx="44" cy="20" rx="14" ry="20" fill="var(--paw-brown)"/>
      <ellipse cx="77" cy="20" rx="14" ry="20" fill="var(--paw-brown)"/>
      <ellipse cx="105" cy="42" rx="13" ry="19" fill="var(--paw-brown)"/>
      <path d="M60 50 C80 50 104 76 100 94 C97 108 78 100 60 100 C42 100 23 108 20 94 C16 76 40 50 60 50 Z" fill="var(--paw-brown)"/>
    </svg>
    <p class="product-line">Treats for Dogs</p>
  </section>

  <p class="size-caption">Label size 3”x5”</p>

  <section class="label label--full" aria-label="Label, full scale">
    <div class="label__border"></div>
    <div class="label__header" role="img" aria-label="Brown header with swirl and paw-print pattern and a mint dog bone holding the company name">
      <p class="brand-name">The Meadowpaw Snack Co.</p>
    </div>
    <p class="claims">No preservatives- nothing artificial<br>No corn, wheat or soy</p>
    <div class="origin-pill"><span class="origin-pill__small">Made in</span><span class="origin-pill__large">Texas, USA</span></div>
    <svg class="organic-badge" viewBox="0 0 150 118" aria-hidden="true">
      <path d="M5 82 L40 70 L40 98 Z M145 82 L110 70 L110 98 Z" fill="var(--badge-ribbon)"/>
      <circle cx="75" cy="58" r="55" fill="var(--badge-green)"/>
    </svg>
    <svg class="paw-icon" viewBox="0 0 120 108" aria-hidden="true">
      <ellipse cx="15" cy="42" rx="13" ry="19" fill="var(--paw-brown)"/>
      <ellipse cx="44" cy="20" rx="14" ry="20" fill="var(--paw-brown)"/>
      <ellipse cx="77" cy="20" rx="14" ry="20" fill="var(--paw-brown)"/>
      <ellipse cx="105" cy="42" rx="13" ry="19" fill="var(--paw-brown)"/>
      <path d="M60 50 C80 50 104 76 100 94 C97 108 78 100 60 100 C42 100 23 108 20 94 C16 76 40 50 60 50 Z" fill="var(--paw-brown)"/>
    </svg>
    <p class="product-line">Treats for Dogs</p>
  </section>

</main>
</body>
</html>
```